Thank You For Shopping / Hair Care Tips

I need “Thank You For Shopping”
Post cards made for my hair business !
I added pictures of post cards that I really like . I also added my LuzeKora Wigs logo for you guys to use

I want the backside of the flyer to have hair care tips !
I want people to have full directions on how to care for their wigs

Target Market(s)

Im marking to young woman to older middle aged woman
Ages 23-66 . I want my flyer to look mature And classy

Industry/Entity Type

Hair And Beauty

Font styles to use
Serif
Script

Colors
e34699
e34298
e34398

Requirements
Must have
• The flyer must have the Instagram logo with my Instagram name next to it @luze.kora.wigs__
• Also it must have my “Luze Kora Wigs” logo that I’ve uploaded in the pictures section .
• Flyer had to be two sides . One side “ thank you for shopping “ side two “hair care tips”
• My website must be on the flyer - www.luzekorawigs.example
• The flyer must match the colors of my logo
• All white . With the pink and glitter sliver you see on my logo
Nice to have
• Nice to have a glitter border
Should not have
• The flyer should not have different colors that don’t match my logo
• It shouldn’t be made without having my Instagram or website on the flyer

```html
<!DOCTYPE html>
<html lang="en">
<head>
<meta charset="utf-8">
<title>Luze Kora Wigs – Thank You / Hair Care Tips Cards</title>
<link rel="stylesheet" href="https://fonts.googleapis.com/css2?family=Playball&family=Montserrat:wght@500;600;700&display=swap">
<style>
  :root {
    --backdrop: #c6beb2;
    --card-dark: #2d2c33;
    --brand-pink: #e3429a;
    --text-white: #ffffff;
    --glitter-purple: #6a2a86;
    --glitter-violet: #5a3f9e;
    --glitter-blue: #3f7fc0;
    --glitter-sky: #7ec3e6;
  }
  * { box-sizing: border-box; margin: 0; padding: 0; }
  html, body {
    width: 1200px; height: 900px; overflow: hidden;
    background: var(--backdrop);
  }
  .canvas { position: relative; width: 1200px; height: 900px; }
  .postcard {
    position: absolute; top: 289px;
    width: 529px; height: 352px;
    box-shadow: 3px 4px 6px rgba(0,0,0,0.35);
  }
  .postcard--thanks { left: 43px; }
  .postcard--tips { left: 635px; }
  .glitter-border {
    position: absolute; inset: 0;
    background: linear-gradient(160deg, var(--glitter-purple) 0%, var(--glitter-violet) 35%, var(--glitter-blue) 70%, var(--glitter-sky) 100%);
  }
  .card-face {
    position: absolute; left: 14px; top: 14px; right: 14px; bottom: 14px;
    background: var(--card-dark);
  }
  .card-title {
    position: absolute; left: 0; right: 0; top: 32px;
    text-align: center;
    font-family: "Playball", cursive;
    font-size: 46px; line-height: 1;
    color: var(--brand-pink);
  }
  .social-band {
    position: absolute; left: 0; right: 0; top: 122px; height: 53px;
    background: var(--brand-pink);
    display: flex; align-items: center; justify-content: center; gap: 12px;
    font-family: "Montserrat", sans-serif; font-weight: 600;
    font-size: 27px; color: var(--text-white);
  }
  .social-mark { width: 24px; height: 24px; display: block; }
  .website-info {
    position: absolute; left: 16px; top: 232px;
    font-family: "Montserrat", sans-serif; color: var(--text-white);
  }
  .website-lead { font-size: 16px; font-weight: 500; }
  .website-url { font-size: 23px; font-weight: 700; margin-top: 8px; }
  .brand-name {
    position: absolute; right: 16px; top: 228px; width: 110px;
    text-align: center;
    font-family: "Montserrat", sans-serif; font-weight: 600;
    font-size: 20px; line-height: 1.15;
    color: var(--brand-pink);
  }
</style>
</head>
<body>
<main class="canvas">
  <section class="postcard postcard--thanks">
    <div class="glitter-border" role="img" aria-label="Purple to blue glitter border"></div>
    <div class="card-face">
      <h1 class="card-title">Thank You For Shopping</h1>
      <div class="social-band">
        <svg class="social-mark" viewBox="0 0 24 24" aria-hidden="true"><rect x="2" y="2" width="20" height="20" rx="3" fill="none" stroke="#fff" stroke-width="2.4"/></svg>
        <span>@luze.kora.wigs__</span>
      </div>
      <div class="website-info">
        <p class="website-lead">For more information visit por website</p>
        <p class="website-url">www.luzekorawigs.example</p>
      </div>
      <p class="brand-name">Luze Kora Wigs</p>
    </div>
  </section>

  <section class="postcard postcard--tips">
    <div class="glitter-border" role="img" aria-label="Purple to blue glitter border"></div>
    <div class="card-face">
      <h2 class="card-title">Hair Care Tips</h2>
      <div class="social-band">
        <svg class="social-mark" viewBox="0 0 24 24" aria-hidden="true"><rect x="2" y="2" width="20" height="20" rx="3" fill="none" stroke="#fff" stroke-width="2.4"/></svg>
        <span>@luze.kora.wigs__</span>
      </div>
      <div class="website-info">
        <p class="website-lead">For more information visit por website</p>
        <p class="website-url">www.luzekorawigs.example</p>
      </div>
      <p class="brand-name">Luze Kora Wigs</p>
    </div>
  </section>
</main>
</body>
</html>
```